Business Card Design Project

Hello! We need a business card design for a new company opening up in Downtown Dallas called Marbury Cupcakes. We are a cupcake factory and our primary colors are Tiffany Blue and Brown. We want to have a design that can be used for multiple positions (Owner/Operations Manager, Assistant Operations Manager, Decorator, Baker, Corporate Sale Rep, Special Events Rep etc) We would like for it to be double sided. Use the following information in your designs:

Renata Vankirk
Assistant Operations Manager
renata@marburycupcakes.example
T555.318.4907

Store Hours:
Mon-Thur 10am-9pm
Fri-Sat 10am-10pm
Sun 12pm-7pm

website: www.marburycupcakes.example

Address: 2735 Birch Ave, Dallas TX 70519

The logo is attached.

Industry/Entity Type

Business

Requirements
Must have
• It must be Tiffany Blue and Brown.
Nice to have
• Nice for it to be double sided.
Should not have
• No graphics like a cupcake. Just the word logo.

```html
<!DOCTYPE html>
<html lang="en">
<head>
<meta charset="utf-8">
<title>Marbury Cupcakes – Business Cards</title>
<link rel="stylesheet" href="https://fonts.googleapis.com/css2?family=Jost:wght@400;500;600&display=swap">
<style>
  :root {
    --tiffany: #8cc4cc;
    --tiffany-deep: #7fbac3;
    --brown: #3d2119;
    --ink: #2b2320;
    --paper: #ffffff;
    --stage: #ece7e2;
  }
  * { box-sizing: border-box; margin: 0; padding: 0; }
  html, body { width: 1200px; height: 508px; overflow: hidden; }
  body {
    background: var(--stage);
    font-family: "Jost", "Futura", sans-serif;
    color: var(--ink);
    position: relative;
  }
  .card {
    position: absolute;
    width: 363px;
    height: 208px;
    overflow: hidden;
    box-shadow: 0 2px 6px rgba(0,0,0,.18);
  }
  .card--front   { left: 423px; top: 26px;  background: var(--paper); }
  .card--blue    { left: 31px;  top: 260px; background: var(--tiffany); }
  .card--brown   { left: 425px; top: 260px; background: var(--brown); }
  .card--white   { left: 814px; top: 260px; background: var(--paper); }

  .wordmark {
    position: absolute;
    text-align: right;
    font-weight: 400;
    line-height: 1;
    color: var(--tiffany-deep);
  }
  .wordmark__name { display: block; font-size: 46px; letter-spacing: .5px; }
  .wordmark__sub  { display: block; font-size: 22px; margin-top: 2px; }
  .card--front .wordmark { left: 36px; top: 14px; width: 290px; }
  .card--blue .wordmark,
  .card--brown .wordmark,
  .card--white .wordmark { left: 50px; top: 30px; width: 250px; }
  .card--blue .wordmark { color: var(--paper); }

  /* front contact block */
  .contact-person {
    position: absolute; right: 184px; top: 127px; text-align: right;
  }
  .contact-person__name { font-size: 13.5px; font-weight: 500; color: var(--tiffany-deep); line-height: 16px; }
  .contact-person__role { font-size: 10.5px; color: var(--ink); line-height: 14px; }
  .contact-person__mail { font-size: 10px; color: var(--ink); line-height: 14px; margin-top: 8px; display: flex; align-items: center; justify-content: flex-end; gap: 4px; white-space: nowrap; }
  .contact-divider {
    position: absolute; left: 190px; top: 127px; width: 1px; height: 52px; background: #cfcfcf;
  }
  .contact-list {
    position: absolute; left: 197px; top: 127px; list-style: none;
    font-size: 10.5px; line-height: 18px; white-space: nowrap;
  }
  .contact-list li { display: flex; align-items: center; gap: 5px; }
  .icon { width: 8px; height: 8px; flex: none; }
  .front-rule { position: absolute; left: 0; right: 0; top: 185px; height: 1px; background: var(--tiffany); }
  .front-band { position: absolute; left: 0; right: 0; top: 188px; bottom: 0; background: var(--brown); }

  /* backs */
  .site {
    position: absolute; left: 0; right: 0; text-align: center;
    font-size: 12.5px; letter-spacing: 2px;
  }
  .card--blue .site  { top: 138px; color: var(--ink); }
  .card--brown .site { top: 127px; color: var(--paper); }
  .card--white .site { top: 128px; color: var(--ink); }

  .hours { position: absolute; left: 0; right: 0; text-align: center; font-size: 10px; white-space: nowrap; }
  .hours b { font-weight: 600; }
  .hours__title { font-size: 12px; font-weight: 600; }
  .card--blue .hours  { top: 164px; color: var(--ink); }
  .card--blue .hours__title { color: var(--brown); margin-bottom: 2px; }
  .card--white .hours { top: 154px; color: var(--ink); line-height: 13px; }
  .card--white .hours__title { margin-bottom: 2px; }

  .hours--split { position: absolute; top: 157px; left: 0; right: 0; color: var(--paper); font-size: 10px; white-space: nowrap; }
  .hours--split b { font-weight: 600; }
  .hours--split .hours__title { position: absolute; right: 188px; top: 0; font-size: 12px; font-weight: 500; }
  .hours--split .hours__rule { position: absolute; left: 181px; top: 2px; width: 1px; height: 34px; background: rgba(255,255,255,.6); }
  .hours--split .hours__list { position: absolute; left: 190px; top: 0; line-height: 12px; }
</style>
</head>
<body>

<section class="card card--front" aria-label="Business card front">
  <div class="wordmark"><span class="wordmark__name">Marbury</span><span class="wordmark__sub">Cupcakes</span></div>

  <div class="contact-person">
    <p class="contact-person__name">Renata Vankirk</p>
    <p class="contact-person__role">Assistant Operations Manager</p>
    <p class="contact-person__mail">
      <svg class="icon" viewBox="0 0 8 8"><rect x="0.5" y="1.5" width="7" height="5" fill="var(--tiffany)"/><path d="M.5 1.5 4 4.5 7.5 1.5" stroke="#fff" fill="none" stroke-width=".8"/></svg>
      renata@marburycupcakes.example
    </p>
  </div>
  <div class="contact-divider"></div>
  <ul class="contact-list">
    <li><svg class="icon" viewBox="0 0 8 8"><path d="M1.5 0.5h1.5l.6 1.8-1 .8a5 5 0 0 0 2.3 2.3l.8-1 1.8.6V6.5a1 1 0 0 1-1 1A6 6 0 0 1 .5 1.5a1 1 0 0 1 1-1z" fill="var(--tiffany)"/></svg>555.318.4907</li>
    <li><svg class="icon" viewBox="0 0 8 8"><circle cx="4" cy="4" r="3.6" fill="var(--tiffany)"/><circle cx="4" cy="3.6" r="1.2" fill="#fff"/></svg>2735 Birch Ave, Dallas TX 70519</li>
    <li><svg class="icon" viewBox="0 0 8 8"><circle cx="4" cy="4" r="3.6" fill="var(--tiffany)"/><path d="M.5 4h7M4 .5c-2 2-2 5 0 7M4 .5c2 2 2 5 0 7" stroke="#fff" stroke-width=".6" fill="none"/></svg>www.marburycupcakes.example</li>
  </ul>
  <div class="front-rule"></div>
  <div class="front-band"></div>
</section>

<section class="card card--blue" aria-label="Business card back, blue">
  <div class="wordmark"><span class="wordmark__name">Marbury</span><span class="wordmark__sub">Cupcakes</span></div>
  <p class="site">www.marburycupcakes.example</p>
  <div class="hours">
    <p class="hours__title">store hours</p>
    <p><b>Mon-Thur</b> 10am-9pm | <b>Fri-Sat</b> 10am-10pm | <b>Sun</b> 12pm-7pm</p>
  </div>
</section>

<section class="card card--brown" aria-label="Business card back, brown">
  <div class="wordmark"><span class="wordmark__name">Marbury</span><span class="wordmark__sub">Cupcakes</span></div>
  <p class="site">www.marburycupcakes.example</p>
  <div class="hours--split">
    <p class="hours__title">store hours</p>
    <span class="hours__rule"></span>
    <div class="hours__list">
      <p><b>Mon-Thur</b> 10am-9pm</p>
      <p><b>Fri-Sat</b> 10am-10pm</p>
      <p><b>Sun</b> 12pm-7pm</p>
    </div>
  </div>
</section>

<section class="card card--white" aria-label="Business card back, white">
  <div class="wordmark"><span class="wordmark__name">Marbury</span><span class="wordmark__sub">Cupcakes</span></div>
  <p class="site">www.marburycupcakes.example</p>
  <div class="hours">
    <p class="hours__title">store hours</p>
    <p><b>Mon-Thur</b> 10am-9pm | <b>Fri-Sat</b> 10am-10pm</p>
    <p><b>Sun</b> 12pm-7pm</p>
  </div>
</section>

</body>
</html>
```